Calloway Brewhouse Beer Can Design

Design a beer can for a boutique craft brewery located in Frankston, Victoria, AUS.
We have a focus on producing Pleasantly Sociable beers in an ambient setting. The beer can design should be sophisticated, simple, recognizable and a little playful. The color pallet should be inviting and not too bold. The design should have identifying features that can be interchanged onto different cans for different beer types. The design must be repeatable for other beer varieties, which will each have a unique color. The can should feature black, white and purple (this should be in interchangeable color). The beer can also needs to have our Calloway Brewhouse company logo on it, this has been attached to the design brief.

Target Market(s)

The target market is aged 25+ who are social, have some disposable income and appreciate good beer, wine and food.
The beers will also be made for distribution, initially to locally to restaurants and cafés and eventually commercially.
Tourists will also be targeted due to the area the brewhouse is located (Mornington Peninsula, Victoria, AUS).

Industry/Entity Type

Hospitality

Font styles to use
Sans Serif
Script

Colors
6b449b
876aae
b7a5cd
e4daeb
000000
ffffff
959595

Requirements
Must have
• The ‘Calloway Brewhouse’ logo.
• The colour associated to this beer - purple. This should be the only colour used on the can (along with black/white/gray).
• The company tagline ‘Pleasantly Sociable’.
• The tasting notes text ‘Bright in colour, dry on the palate and thirst quenching in the extreme, wheat and pale malts compliment each other with nuance.’
• Australian beer can requirements as per 'Requirements.png'. EPS and AI files of the requirements have been included.
Nice to have
• The logo text ‘Wendel Malt IPA’ more predominant than the Calloway Brewhouse logo.
Should not have
• Be busy, simple is best
• Beer related pictures / images
• Bold, masculine lines and fonts
• Requirements.png directly used. Please use the EPS or AI files provided.

```html
<!DOCTYPE html>
<html lang="en">
<head>
<meta charset="utf-8">
<title>Calloway Brewhouse – Wendel Malt IPA 12oz Can Template</title>
<link rel="stylesheet" href="https://fonts.googleapis.com/css2?family=Oswald:wght@300;400&family=Roboto:wght@400;700&display=swap">
<style>
  :root{
    --purple:#6b449b;
    --purple-mid:#876aae;
    --purple-soft:#b7a5cd;
    --purple-pale:#e4daeb;
    --black:#000000;
    --white:#ffffff;
    --grey:#959595;
    --guide:#8f86c9;
    --swatch:#8a99cc;
    --can-limit:#e0282e;
    --copy-limit:#2b2f9a;
    --neck-bend:#1aa34a;
    --overlap:#3bb6e8;
  }
  *{box-sizing:border-box;margin:0;padding:0}
  html,body{width:1200px;height:612px;overflow:hidden;background:var(--white)}
  body{position:relative;font-family:'Roboto',Arial,sans-serif;color:var(--black)}
  .abs{position:absolute}
  .sheet-title{left:0;width:1300px;top:26px;text-align:center;font-weight:700;font-size:13px}

  /* dieline guides */
  .guides{left:0;top:0}
  .guide-label{font-size:5.5px;color:var(--guide);letter-spacing:.2px;white-space:nowrap;background:var(--white);padding:0 2px}
  .guide-label.vertical{transform:rotate(-90deg);transform-origin:left top}

  /* can wrap */
  .wrap{left:63px;top:102px;width:603px;height:326px;background:var(--white);border:1px solid #e6a2b4;overflow:hidden}
  .band-top{left:0;top:0;width:100%;height:50px;background:var(--purple)}
  .stripe{left:0;width:100%;height:6px;background:var(--purple-soft)}
  .band-bottom{left:0;top:244px;width:100%;height:82px;background:var(--purple)}

  .tasting-notes{left:64px;top:74px;width:128px;font-size:5.6px;line-height:1.35}
  .brand-mark{font-family:'Oswald',sans-serif;font-weight:300;text-align:center;line-height:1}
  .brand-mark .name{display:block;font-size:21px;letter-spacing:.5px}
  .brand-mark .sub{display:block;font-size:7px;letter-spacing:2.4px;margin-top:3px}
  .brand-front{left:238px;top:75px;width:150px;color:var(--black)}
  .beer-name{left:213px;top:124px;width:200px;text-align:center;font-family:'Oswald',sans-serif;font-weight:300;font-size:45px;line-height:1.08;color:var(--purple)}

  .made-in{left:64px;top:199px;font-size:5.8px;line-height:1.45}
  .made-in strong{font-weight:700}
  .social{display:flex;align-items:center;gap:4px;margin-top:3px;color:var(--purple);font-weight:700}
  .social .dot{width:8px;height:8px;background:var(--purple)}

  .ingredients{left:433px;top:73px;font-size:5.4px;line-height:1.35}
  .ingredients strong{font-weight:700}
  .badges{left:433px;top:110px;display:flex;gap:8px;align-items:center}
  .badge{width:27px;height:27px;background:var(--black)}
  .badge.round{border-radius:50%;background:var(--grey)}
  .badge.outline{background:var(--white);border:2px solid var(--black);border-radius:4px}
  .refund{left:432px;top:153px;display:flex;gap:3px;align-items:center}
  .refund .value{font-family:'Oswald',sans-serif;font-weight:400;font-size:14px}
  .refund .terms{width:60px;font-size:3.6px;line-height:1.2;text-transform:uppercase}
  .abv-small{left:433px;top:177px;font-size:5.8px}
  .std-label{left:520px;top:228px;transform:rotate(-90deg);transform-origin:left top;font-family:'Oswald',sans-serif;font-size:9px;white-space:nowrap}
  .std-glass{left:533px;top:151px}

  .brand-back{left:40px;top:262px;width:150px;color:var(--white)}
  .tagline{left:213px;top:253px;width:200px;text-align:center;font-family:'Oswald',sans-serif;font-weight:300;font-size:15px;letter-spacing:.4px;color:var(--white)}
  .volume{left:249px;top:299px;font-size:8.5px;color:var(--white)}
  .abv{left:333px;top:299px;font-size:8.5px;color:var(--white)}
  .name-back{left:430px;top:267px;width:150px;text-align:center;font-family:'Oswald',sans-serif;font-weight:300;font-size:17px;color:var(--white);letter-spacing:.3px}

  /* printer notes */
  .upc-info{left:449px;top:462px;width:228px;font-size:6.8px;line-height:1.3}
  .upc-info h3{font-size:7.4px;font-weight:700}
  .note-box{left:445px;top:497px;width:235px;height:59px;border:1px solid #cfcfcf;padding:3px 5px;font-size:5.2px;line-height:1.35}
  .note-box h4,.print-note h4{font-size:6.6px;font-weight:700}
  .note-box .lead{font-size:6.2px;font-weight:700}
  .print-note{left:449px;top:561px;width:240px;font-size:6.4px;line-height:1.3;font-weight:700}

  .job-table{left:72px;top:517px;width:281px;border-collapse:collapse;font-size:7px;table-layout:fixed}
  .job-table td,.job-table th{border:1px solid var(--black);height:9.5px;line-height:8px;padding:0 3px;text-align:left;font-weight:400}
  .job-table th{background:var(--black);color:var(--white);font-weight:700}
  .job-table .label-strong{font-weight:700}
  .job-table .pms{width:34px;text-align:center}
  .job-table .swatch{width:43px;background:var(--swatch);border-top-color:var(--swatch);border-bottom-color:var(--swatch)}

  .legend{left:365px;top:517px;width:76px;height:77px;border:1px solid #bdbdbd;padding:4px 4px;font-size:5.4px;font-weight:700}
  .legend-row{display:flex;align-items:center;gap:5px;margin-bottom:6px}
  .legend-row .line{width:20px;height:1px}
  .legend-row.can{color:var(--can-limit)} .legend-row.can .line{background:var(--can-limit)}
  .legend-row.copy{color:var(--copy-limit)} .legend-row.copy .line{background:var(--copy-limit)}
  .legend-row.neck{color:var(--neck-bend)} .legend-row.neck .line{background:var(--neck-bend)}
  .legend-row.over{color:var(--overlap);align-items:flex-start;line-height:1.15}
  .hatch{flex:none;width:20px;height:18px;background:repeating-linear-gradient(135deg,var(--overlap) 0 1.5px,transparent 1.5px 4px)}
  .legend-row.over small{font-size:4.4px;font-weight:400}
</style>
</head>
<body>
  <div class="abs sheet-title">12oz Beverage Can Template</div>

  <svg class="abs guides" width="720" height="460" aria-hidden="true">
    <g stroke="var(--guide)" stroke-width=".6" fill="none">
      <line x1="63" y1="93" x2="666" y2="93" stroke-dasharray="2 2"/>
      <line x1="63" y1="90" x2="63" y2="96"/><line x1="666" y1="90" x2="666" y2="96"/>
      <line x1="45" y1="102" x2="45" y2="428" stroke-dasharray="2 2"/>
      <line x1="56" y1="110" x2="56" y2="420" stroke-dasharray="2 2"/>
      <line x1="92" y1="437" x2="640" y2="437" stroke-dasharray="2 2"/>
      <line x1="63" y1="446" x2="666" y2="446" stroke-dasharray="2 2"/>
    </g>
    <path d="M681 102 h14 q5 0 5 6 v22 q0 6 6 10 q6 4 6 10 v264 q0 6 -6 10 q-6 4 -6 10 v0 q0 6 -5 6 h-14" stroke="var(--black)" stroke-width=".8" fill="none"/>
    <line x1="666" y1="357" x2="680" y2="357" stroke="#cfcfcf" stroke-width=".6"/>
    <line x1="680" y1="357" x2="680" y2="497" stroke="#cfcfcf" stroke-width=".6"/>
  </svg>
  <div class="abs guide-label" style="left:90px;top:89px">OVERLAP (0.3248")</div>
  <div class="abs guide-label" style="left:583px;top:89px">OVERLAP (0.2061")</div>
  <div class="abs guide-label vertical" style="left:41px;top:300px">LITHO LIMITS (4.5179")</div>
  <div class="abs guide-label vertical" style="left:52px;top:300px">TYPE LIMITS (4.2177")</div>
  <div class="abs guide-label" style="left:328px;top:433px">TYPE LIMITS (7.6891")</div>
  <div class="abs guide-label" style="left:328px;top:442px">LITHO LIMITS (8.3785")</div>

  <section class="abs wrap">
    <div class="abs band-top"></div>
    <div class="abs stripe" style="top:50px"></div>
    <div class="abs stripe" style="top:238px"></div>
    <div class="abs band-bottom"></div>

    <p class="abs tasting-notes">Bright in colour, dry on the palate and thirst quenching in the extreme, wheat and pale malts compliment each other with nuance.</p>

    <div class="abs brand-mark brand-front"><span class="name">Calloway</span><span class="sub">BREWHOUSE</span></div>
    <h1 class="abs beer-name">WENDEL<br>MALT IPA</h1>

    <div class="abs made-in">
      <strong>Made in:</strong><br>Mornington Peninsula, Victoria, AUS
      <div class="social"><span class="dot"></span>Calloway Brewhouse</div>
    </div>

    <div class="abs ingredients"><strong>INGREDIENTS:</strong><br>Malt, hops.</div>
    <div class="abs badges">
      <span class="badge"></span>
      <span class="badge round"></span>
      <svg width="28" height="26" viewBox="0 0 28 26" aria-label="Recycle icon" role="img">
        <g fill="none" stroke="var(--black)" stroke-width="3">
          <path d="M9 4 L14 2 L19 9"/><path d="M23 13 L25 19 L16 22"/><path d="M11 22 L3 19 L7 11"/>
        </g>
      </svg>
      <span class="badge outline"></span>
    </div>
    <div class="abs refund"><span class="value">10c</span><span class="terms">Refund at collection depots when sold in participating states</span></div>
    <div class="abs abv-small">4.8% ABV</div>

    <div class="abs std-label">Standard Drinks</div>
    <svg class="abs std-glass" width="40" height="76" viewBox="0 0 40 76" aria-label="Standard drinks: 1.2" role="img">
      <path d="M2 2 H38 L33 74 H7 Z" fill="var(--black)"/>
      <path d="M8 8 H32 L28 68 H12 Z" fill="var(--white)"/>
      <rect x="10" y="12" width="20" height="18" fill="var(--black)"/>
      <text x="20" y="25" text-anchor="middle" font-family="Oswald, sans-serif" font-size="10" fill="var(--white)">1.2</text>
      <text x="20" y="64" text-anchor="middle" font-family="Roboto, sans-serif" font-size="4" fill="var(--black)">330ml</text>
    </svg>

    <div class="abs brand-mark brand-back"><span class="name">Calloway</span><span class="sub">BREWHOUSE</span></div>
    <div class="abs tagline">Pleasantly Sociable</div>
    <div class="abs volume">355 ml</div>
    <div class="abs abv">4.7% ABV</div>
    <div class="abs name-back">WENDEL MALT IPA</div>
  </section>

  <div class="abs upc-info">
    <h3>UPC INFORMATION</h3>
    <p>The UPC is 100% and non-truncated with a white background. Anything smaller or with a non-white background will require a signed waiver letter. White counts as one of the six colors.</p>
  </div>
  <div class="abs note-box">
    <h4>***NOTE***</h4>
    <p class="lead">A 100% full size barcode will fit within this box size.</p>
    <p>Box measurement = ( 1.0656" x 1.5058").</p>
    <p style="margin-top:3px">If you are unable to generate a barcode, Arbor Graphics can do this for you. All that is required is the barcode number and the placement of the box within your design.</p>
  </div>
  <div class="abs print-note">
    <h4>***NOTE***</h4>
    <p>In order to produce the highest quality can possible, Arbor Closure &amp; Seal, Inc. reserves the right to make minor adjustments to customer supplied artwork to meet our print production requirements.</p>
  </div>

  <table class="abs job-table">
    <tr><th>JOB INFORMATION</th><th class="pms">PMS #</th><th style="width:43px">SWATCH</th></tr>
    <tr><td class="label-strong">CLIENT NAME</td><td class="pms">####</td><td class="swatch"></td></tr>
    <tr><td>DESIGN NAME</td><td class="pms">####</td><td class="swatch"></td></tr>
    <tr><td>DATE</td><td class="pms">####</td><td class="swatch"></td></tr>
    <tr><td rowspan="4" style="vertical-align:top">ADDITIONAL COMMENTS</td><td class="pms">####</td><td class="swatch"></td></tr>
    <tr><td class="pms">####</td><td class="swatch"></td></tr>
    <tr><td class="pms">####</td><td class="swatch"></td></tr>
    <tr><td class="pms">####</td><td class="swatch"></td></tr>
  </table>

  <div class="abs legend">
    <div class="legend-row can"><span class="line"></span>CAN LIMIT</div>
    <div class="legend-row copy"><span class="line"></span>COPY LIMIT</div>
    <div class="legend-row neck"><span class="line"></span>NECK BEND</div>
    <div class="legend-row over"><span class="hatch"></span><span>OVERLAP<br><small>(Reference Guideline Pocket for Handling This Area)</small></span></div>
  </div>
</body>
</html>
```